Flyer Design

Mobile (Dustless) Shot Blasting.Graffiti Removal, Brick and Stone restoration, Paint Stripping from garden gates to Ships.No job too big or Small.No Chemicals - just Air, Water and recycled abrasive.Fully pressure controlled to prevent damage to underlying surfaces.

Target Market(s)

Domestic and commercial

Industry/Entity Type

Paint

Requirements
Nice to have
• Before and after paint removal to bare steel.
• Before and after cleaned brick/ stone work and graffiti removal

```html
<!DOCTYPE html>
<html lang="en">
<head>
<meta charset="utf-8">
<title>Mobile Dustless Shot Blasting Flyer</title>
<link rel="stylesheet" href="https://fonts.googleapis.com/css2?family=Oswald:wght@500;700&family=Open+Sans:wght@400;700&family=Kalam:wght@400&family=Architects+Daughter&family=Bowlby+One&display=swap">
<style>
:root{
  --green:#2e9b3e;
  --green-light:#4cb84e;
  --red:#e3242b;
  --black:#111111;
  --yellow:#f7b524;
  --white:#ffffff;
  --photo-frame:#f7b524;
  --silver:#c9cbcc;
}
*{margin:0;padding:0;box-sizing:border-box}
html,body{width:1200px;height:806px;overflow:hidden;background:#e9e9e9}
.flyer{position:relative;width:1200px;height:806px;overflow:hidden;
  background:radial-gradient(ellipse at 50% 45%,var(--green-light),var(--green) 70%);font-family:"Open Sans",sans-serif}
.top-strip{position:absolute;left:0;top:0;width:1200px;height:22px;background:var(--green-light)}
.title-band{position:absolute;left:0;top:22px;width:1200px;height:85px;background:var(--red)}
.title{position:absolute;left:144px;top:32px;font-family:"Oswald",sans-serif;font-weight:700;font-size:50px;color:var(--white);letter-spacing:1px;line-height:1;transform:scaleX(.8);transform-origin:left;white-space:nowrap}
.info-band{position:absolute;left:0;top:107px;width:1200px;height:59px;background:var(--black)}
.eco-label{position:absolute;left:0;top:107px;width:259px;height:59px;background:var(--yellow);clip-path:polygon(0 0,100% 0,93% 100%,0 100%);
  font-weight:700;font-size:27px;color:var(--black);padding:12px 0 0 18px}
.eco-text{position:absolute;left:280px;top:120px;font-size:23px;color:var(--white)}
.brand{position:absolute;left:866px;top:16px;width:290px;height:158px;border-radius:50%;background:var(--black);border:7px solid var(--silver);
  display:flex;align-items:center;justify-content:center;gap:10px}
.brand-dot{width:22px;height:22px;border-radius:50%;background:var(--green-light)}
.brand-name{font-family:"Open Sans",sans-serif;font-weight:700;font-size:24px;color:var(--white)}
.tagline{position:absolute;left:0;width:1200px;top:196px;text-align:center;font-family:"Kalam",cursive;font-size:36px;color:var(--white);white-space:nowrap}
.service{position:absolute;top:267px;width:251px}
.service-photo{height:238px;border:4px solid var(--photo-frame);border-radius:16px}
.service-label{margin:2px auto 0;width:203px;height:62px;background:var(--red);border-radius:0 0 12px 12px;
  font-family:"Oswald",sans-serif;font-weight:500;font-size:21px;line-height:24px;color:var(--white);text-align:center;padding-top:7px;text-transform:uppercase}
.s1{left:57px}.s2{left:335px}.s3{left:615px}.s4{left:893px}
.s1 .service-photo{background:linear-gradient(160deg,#c9c3b4,#8e8a80)}
.s2 .service-photo{background:linear-gradient(120deg,#d7c79b,#8c7d58)}
.s3 .service-photo{background:linear-gradient(180deg,#9fb7c4 0%,#7a6f68 45%,#8a4a3a 100%)}
.s4 .service-photo{background:linear-gradient(180deg,#c7cbd0 0%,#f0ede2 45%,#3f6aa2 80%,#6c6a66 100%)}
.slogan{position:absolute;left:16px;top:616px;font-family:"Bowlby One",sans-serif;font-size:33px;line-height:40px;transform:rotate(-5deg);transform-origin:left;white-space:nowrap}
.slogan span{display:block}
.slogan .a{color:#e4e4e4}.slogan .b{color:#e4e4e4}.slogan .c{color:var(--red)}
.why{position:absolute;left:254px;top:748px;font-family:"Oswald",sans-serif;font-weight:700;font-size:15px;color:var(--black);transform:rotate(-90deg);transform-origin:left top;white-space:nowrap}
.benefits{position:absolute;left:280px;top:605px;list-style:none;font-family:"Architects Daughter",cursive;font-size:14px;line-height:25.5px;color:var(--white);text-transform:uppercase;white-space:nowrap}
.benefits li{display:flex;align-items:center;gap:8px}
.benefits svg{flex:none}
.equipment{position:absolute;left:602px;top:580px;width:225px;height:212px;border-radius:8px;background:linear-gradient(180deg,#2fb24a 0%,#1c7a30 60%,#2a2a2a 100%)}
.mobile-band{position:absolute;left:806px;top:624px;width:394px;height:88px;background:var(--yellow);
  font-weight:700;font-size:17px;line-height:22px;color:var(--black);text-align:right;padding:11px 12px 0 0;text-transform:uppercase}
.tow-band{position:absolute;left:830px;top:712px;width:370px;height:36px;background:var(--red);
  font-weight:700;font-size:17px;color:var(--white);text-align:right;padding:6px 12px 0 0}
.bottom-band{position:absolute;left:0;top:761px;width:1200px;height:45px;background:var(--black)}
</style>
</head>
<body>
<main class="flyer">
  <div class="top-strip"></div>
  <div class="title-band"></div>
  <h1 class="title">MOBILE (DUSTLESS) SHOT BLASTING</h1>
  <div class="info-band"></div>
  <div class="eco-label">ECO - FRIENDLY</div>
  <p class="eco-text">No Chemicals - just Air, Water and recycled abrasive.</p>
  <div class="brand"><span class="brand-dot"></span><span class="brand-name">Cascade Blasting</span></div>

  <p class="tagline">Fully pressure controlled to prevent damage to underlying surfaces.</p>

  <section class="service s1"><div class="service-photo" role="img" aria-label="Worker blasting graffiti off a stone block wall"></div><div class="service-label">Graffiti<br>Removal</div></section>
  <section class="service s2"><div class="service-photo" role="img" aria-label="Brick and stone wall half cleaned"></div><div class="service-label">Brick and Stone<br>Restoration</div></section>
  <section class="service s3"><div class="service-photo" role="img" aria-label="Worker in protective suit stripping paint from a metal garden gate"></div><div class="service-label">Paint Stripping<br>from Garden Gates</div></section>
  <section class="service s4"><div class="service-photo" role="img" aria-label="Sailing boat hull on stands with paint stripped"></div><div class="service-label">Paint Stripping<br>from Ships</div></section>

  <div class="slogan"><span class="a">NO JOB</span><span class="b">TOO BIG</span><span class="c">OR SMALL</span></div>
  <div class="why">WHY DUSTLESS?</div>
  <ul class="benefits">
    <li><svg width="13" height="13" viewBox="0 0 14 14"><circle cx="7" cy="7" r="5.5" fill="none" stroke="#f7b524" stroke-width="2.5"/></svg>It is eco-friendly</li>
    <li><svg width="13" height="13" viewBox="0 0 14 14"><circle cx="7" cy="7" r="5.5" fill="none" stroke="#f7b524" stroke-width="2.5"/></svg>Creates less mess</li>
    <li><svg width="13" height="13" viewBox="0 0 14 14"><circle cx="7" cy="7" r="5.5" fill="none" stroke="#f7b524" stroke-width="2.5"/></svg>Does not kill grass</li>
    <li><svg width="13" height="13" viewBox="0 0 14 14"><circle cx="7" cy="7" r="5.5" fill="none" stroke="#f7b524" stroke-width="2.5"/></svg>Will not warp metal</li>
    <li><svg width="13" height="13" viewBox="0 0 14 14"><circle cx="7" cy="7" r="5.5" fill="none" stroke="#f7b524" stroke-width="2.5"/></svg>Will not demage gel coat</li>
    <li><svg width="13" height="13" viewBox="0 0 14 14"><circle cx="7" cy="7" r="5.5" fill="none" stroke="#f7b524" stroke-width="2.5"/></svg>It is faster than other methods</li>
  </ul>

  <div class="mobile-band">Since we are mobile we can<br>come to you and blast your<br>boat right where it is.</div>
  <div class="tow-band">NO NEED TO TOW IT TO US.</div>
  <div class="bottom-band"></div>
  <div class="equipment" role="img" aria-label="Green mobile dustless blasting unit on a trailer"></div>
</main>
</body>
</html>
```